Power Point Presentation or Canva Slides

Project: Photography Brochure (10-12 pages, A4 size)

Objective: To create a clean, high-end, and easy-to-read PDF brochure showcasing headshot packages for corporate clients, emphasizing value, quality, and a stress-free process.

Project content, logos, brand colours and images can be found here: https://files.vorneluxa.com/open?id=84kPq27TfmwjXbRtLcVNsYe5hd1GuQzOp&src=vault_ls

Design Direction
* Overall Style: Minimal, sophisticated, and modern.
* Use plenty of whitespace to create a breathable layout.

* Professional yet approachable tone.

* High-end look to convey quality and professionalism.

* Ensure text is easy to skim with clear headlines, subheadings, and icons where applicable.

Key Focus Areas:
* Emphasize value the client receives (not just prices).
* Ease of process and genuine expressions are key selling points.
* Testimonials should be scattered throughout as visual callouts, not in blocks.
* Make sure every page looks visually appealing with an appropriate balance of text and images.

Target Market(s)

Businesses - business owners, marketing managers, executive assistants, 50% male and 50% female

Industry/Entity Type

Commercial photography

Font styles to use
Other font styles liked:
• Helvetica

Requirements
Must have
• Minimal, high-end aesthetic (clear, polished, easy to skim), Consistent typography, spacing, and alignment for a professional look Strong emphasis on value for the client (not just listing features), Breathing room in the layout (not text-heavy or overwhelming), Brand consistency (uses provided colors, fonts, and logos correctly)
Nice to have
• A mix of text + visuals for an engaging layout
Should not have
• generic stock feature images (use the supplied images - stock images are OK ONLY if blurred and used as a background with overlay), ), Overcrowded or cluttered pages, Generic, overused Canva templates that feel cheap, Excessive colors or flashy design elements that distract from the message

```html
<!DOCTYPE html>
<html lang="en">
<head>
<meta charset="utf-8">
<title>Julian Mercer Photography – Corporate Headshot Brochure</title>
<link href="https://fonts.googleapis.com/css2?family=Barlow+Condensed:ital,wght@0,300;0,400;0,500;0,700;1,600;1,700&family=Allura&display=swap" rel="stylesheet">
<style>
  :root{
    --backdrop:#a9a9a9;
    --paper:#ffffff;
    --ink:#111111;
    --green:#45c39a;
    --teal:#2fb7c7;
    --teal-mid:#3bbcae;
    --photo-dark:#2d3b3a;
    --photo-mid:#6f7d7a;
    --white:#ffffff;
  }
  *{margin:0;padding:0;box-sizing:border-box}
  html,body{width:1200px;height:2252px;overflow:hidden;background:var(--backdrop)}
  body{position:relative;font-family:"Barlow Condensed",Arial,sans-serif;color:var(--ink)}
  .page{position:absolute;left:235px;width:730px;background:var(--paper);overflow:hidden}
  .page--cover{top:75px;height:1032px}
  .page--intro{top:1142px;height:1033px}
  .abs{position:absolute}

  /* cover */
  .cover-shapes{position:absolute;inset:0;width:730px;height:1032px}
  .cover-title{left:40px;top:36px;color:var(--white);line-height:1}
  .cover-title .t1{display:block;font-weight:300;font-size:90px;letter-spacing:1px}
  .cover-title .t2{display:block;font-weight:400;font-size:46px;margin-top:-4px}
  .cover-title .t3{display:block;font-weight:700;font-size:66px;color:var(--ink);margin-top:2px}
  .cover-sub{left:40px;top:248px;font-size:16px;line-height:1.25;color:var(--white);font-weight:400;white-space:nowrap}
  .cover-bar{left:0;top:304px;width:420px;height:30px;background:var(--ink);color:var(--white);font-style:italic;font-weight:600;font-size:18px;line-height:30px;padding-left:38px;white-space:nowrap}
  .brand-mark{left:460px;top:280px;font-weight:400;color:var(--ink);line-height:1}
  .brand-mark .name{display:block;font-size:64px;letter-spacing:1px}
  .brand-mark .trade{display:block;font-size:19px;letter-spacing:9px;margin-top:12px;padding-left:37px}
  .cover-photo{left:40px;top:375px;width:430px;height:657px;border-radius:200px 200px 0 0;background:linear-gradient(180deg,var(--photo-mid),var(--photo-dark))}

  /* intro page */
  .intro-band{left:0;top:40px;width:565px;height:365px;background:linear-gradient(90deg,var(--green),var(--teal))}
  .intro-heading{left:47px;top:66px;font-style:italic;font-weight:700;font-size:50px;line-height:1.14;color:var(--white);white-space:nowrap}
  .intro-copy{left:47px;top:212px;width:445px;font-size:15px;line-height:1.3;color:var(--white)}
  .intro-copy p+p{margin-top:18px}
  .intro-sign{left:47px;top:328px;color:var(--white)}
  .script{font-family:"Allura",cursive;font-size:32px;line-height:1}
  .sign-role{font-size:15px;line-height:1.2}
  .owner-photo{left:512px;top:27px;width:194px;height:657px;border-radius:90px 90px 30px 30px;background:linear-gradient(180deg,var(--photo-mid),var(--photo-dark))}
  .trust-heading{left:47px;top:440px;font-style:italic;font-weight:700;font-size:52px;line-height:1.2;color:var(--ink);white-space:nowrap}
  .trust-list{left:47px;top:586px;list-style:none;font-size:16px;line-height:21px}
  .trust-list li{position:relative;padding-left:22px}
  .trust-list li::before{content:"";position:absolute;left:0;top:10px;width:4px;height:4px;background:var(--ink);border-radius:50%}
  .trust-list b{font-weight:700}
  .quote-band{left:37px;top:729px;width:693px;height:169px;border-radius:84px 0 0 84px;background:linear-gradient(90deg,var(--green),var(--teal))}
  .quote-mark{font-family:Georgia,serif;font-size:170px;line-height:1;color:rgba(255,255,255,.25);font-weight:700}
  .quote-open{left:160px;top:700px}
  .quote-close{left:612px;top:830px}
  .client-ring{left:37px;top:739px;width:150px;height:150px;border-radius:50%;background:var(--white);border:5px solid var(--teal-mid);padding:5px}
  .client-photo{width:100%;height:100%;border-radius:50%;background:linear-gradient(180deg,#8d9594,#3b4544)}
  .quote-text{left:246px;top:745px;width:430px;font-size:15px;line-height:1.3;color:var(--white)}
  .quote-sign{left:246px;top:838px;color:var(--white)}
  .quote-sign .script{font-size:30px}
  .partner-row{left:57px;top:926px;width:640px;height:62px;display:flex;align-items:center;gap:34px}
  .partner{display:flex;align-items:center;gap:8px;font-weight:700;font-size:20px;color:var(--ink)}
  .partner .dot{width:24px;height:24px;background:var(--teal-mid)}
  .partner .dot.round{border-radius:50%}
  .review-badge{width:130px;height:44px;border-radius:6px;background:#e9eeee;margin-left:auto}
</style>
</head>
<body>

<section class="page page--cover">
  <svg class="cover-shapes" viewBox="0 0 584 826" preserveAspectRatio="none" aria-hidden="true">
    <defs>
      <linearGradient id="brandGrad" x1="0" y1="1" x2="1" y2="0">
        <stop offset="0" stop-color="#45c39a"/>
        <stop offset="1" stop-color="#2fb7c7"/>
      </linearGradient>
    </defs>
    <polygon points="0,0 584,0 0,570" fill="url(#brandGrad)"/>
    <polygon points="307,290 584,470 584,520 270,826 30,826 150,450" fill="url(#brandGrad)"/>
    <polygon points="412,575 532,665 420,826 300,826" fill="url(#brandGrad)"/>
  </svg>

  <h1 class="abs cover-title">
    <span class="t1">CORPORATE</span>
    <span class="t2">HEADSHOT &amp; BRANDING</span>
    <span class="t3">PHOTOGRAPHY</span>
  </h1>
  <p class="abs cover-sub">Professional, approachable, consistent headshots for your team<br>—no awkward or stiff poses</p>
  <div class="abs cover-bar">Easy relaxed process – even if you hate photos</div>

  <div class="abs brand-mark">
    <span class="name">JULIAN</span>
    <span class="name">MERCER</span>
    <span class="trade">PHOTOGRAPHY</span>
  </div>

  <div class="abs cover-photo" role="img" aria-label="Photographer smiling behind a camera mounted on a tripod"></div>
</section>

<section class="page page--intro">
  <div class="abs intro-band"></div>
  <h2 class="abs intro-heading">Outdated, low-quality,<br>or awkward headshots?</h2>
  <div class="abs intro-copy">
    <p>A bad photo sends the wrong message about your company.</p>
    <p>My team and I work with companies to deliver professional, consistent, and natural-looking headshots every time—without the awkwardness. Let's make your team look amazing!</p>
  </div>
  <div class="abs intro-sign">
    <div class="script">Julian Mercer</div>
    <div class="sign-role">Studio Owner</div>
  </div>

  <div class="abs owner-photo" role="img" aria-label="Studio owner standing full length, holding a camera"></div>

  <h2 class="abs trust-heading">WHY 500+<br>COMPANIES TRUST US</h2>
  <ul class="abs trust-list">
    <li><b>Genuine Expressions</b>—No awkward photos here</li>
    <li>Easy, Comfortable Process – even if you hate photos</li>
    <li><b>Consistency</b> —consistent professional results</li>
    <li>Mobile studio—save time &amp; hassle of studio shoots</li>
  </ul>

  <div class="abs quote-band"></div>
  <div class="abs quote-mark quote-open" aria-hidden="true">“</div>
  <div class="abs quote-mark quote-close" aria-hidden="true">”</div>
  <div class="abs client-ring">
    <div class="client-photo" role="img" aria-label="Portrait of the client giving the testimonial"></div>
  </div>
  <blockquote class="abs quote-text">The thought of having a professional photographer come to our business brought back memories of school photos.<br>But Julian made it all very relaxed and easy and readily put us all at ease knowing our faces were in good hands.</blockquote>
  <div class="abs quote-sign">
    <div class="script">Daniel Corrow</div>
    <div class="sign-role">Veltrix</div>
  </div>

  <div class="abs partner-row">
    <span class="partner"><span class="dot"></span>Goldarch</span>
    <span class="partner"><span class="dot round"></span>Ridgeway</span>
    <span class="partner">Cellar Lane</span>
    <span class="partner">Strideon</span>
    <span class="review-badge" aria-hidden="true"></span>
  </div>
</section>

</body>
</html>
```